Brightleaf Homes needs a web design and brand identifier

Brightleaf Homes is a pioneering approach by Victorian councils and four greenhouse alliances to support low income households to install solar systems with no upfront costs.

Brightleaf Homes will commence in May 2017.

Brightleaf Homes is looking for a designer to create a website banner incorporating a brand identifier for Brightleaf Homes. The brand identifier will be used in Brightleaf Homes promotional materials, such as flyers and mail outs.

The website banner and brand identifier should engender trust and confidence in the target group (retirees).
Updates

Project Deadline Extended
Reason: Hi, Thank you for your work so far. We've been given advice to get a separate logo designed (instead of trying to include this as part of the banner design). Sorry for not realising this until now - we're new to all this. So, I have a couple of preliminary logo designs that are being considered by our project control group. I will forward a copy of the logo once we have it. The project control group is looking for a web design that is unique to Brightleaf Homes and a design that draws on the key elements of the program (i.e. it helps people save money and take control). The site should be friendly but not too informal as the target group is seniors. Here's a link to another community energy organisation: www.kelvowattgroup.com.au/ Apologies again for the delays. Cheers, Tomas

Target Market(s)

Home owning, low income, retirees

Industry/Entity Type

Non Profit

Number of Pages Required

1 page

Font styles to use
Sans Serif

Requirements
Must have
• Use of Brightleaf Home name
• Must promote Brightleaf Homes as safe, reliable and trustworthy
Nice to have
• Blue - to engender sense of safety and confidence (open to suggestions, though)
• Solar panels / the sun
Should not have
• Anything that is hard to read
• anything that promotes riskyness

```html
<!DOCTYPE html>
<html lang="en">
<head>
<meta charset="utf-8">
<title>Brightleaf Homes</title>
<link rel="stylesheet" href="https://fonts.googleapis.com/css2?family=Roboto:wght@400;500;700&family=Open+Sans:wght@400;600&display=swap">
<style>
:root{
  --blue:#3f6fc6;
  --green:#1aa27a;
  --grey-icon:#7b7b7b;
  --grey-btn:#8a8a8a;
  --text:#333;
  --muted:#555;
  --light-bg:#efefef;
  --footer:#3a3a3a;
  --white:#fff;
  --stream-fill:#eef2fa;
}
*{box-sizing:border-box;margin:0;padding:0}
html,body{width:1200px;height:2985px;overflow:hidden;background:var(--white)}
body{font-family:"Open Sans",Arial,sans-serif;color:var(--text)}
.page{width:1200px;height:2985px;position:relative}

/* header */
.site-header{height:130px;position:relative}
.brand{position:absolute;left:100px;top:50px;display:flex;align-items:center;gap:12px}
.brand-square{width:34px;height:34px;background:var(--blue);border-radius:4px}
.brand-name{font-family:"Roboto",sans-serif;font-weight:700;font-size:26px;color:var(--blue);letter-spacing:.5px}
.contact{position:absolute;right:96px;top:22px;display:flex;align-items:center;gap:14px;font-family:"Roboto",sans-serif;font-size:15px}
.contact .item{display:flex;align-items:center;gap:10px}
.contact .dot{width:32px;height:32px;border-radius:50%;display:flex;align-items:center;justify-content:center}
.contact .mail .dot{background:var(--blue)}
.contact .mail{color:var(--blue)}
.contact .phone .dot{border:2px solid #222}
.contact .phone{font-size:17px;font-weight:500;color:#222;margin-left:12px}
.main-nav{position:absolute;right:92px;top:88px;display:flex;gap:46px;font-family:"Roboto",sans-serif;font-size:14px;color:#222}
.main-nav .active{color:var(--blue)}

/* hero */
.hero{height:485px;position:relative;background:linear-gradient(90deg,#7f87a6 0%,#9aa3bd 40%,#c9cfdc 70%,#b7c0d1 100%);overflow:hidden}
.hero .photo{position:absolute;inset:0;background:linear-gradient(180deg,rgba(180,190,215,.6) 0%,rgba(150,160,190,.3) 50%,rgba(70,120,50,.8) 78%,#4f8a2e 100%)}
.hero-content{position:absolute;left:100px;top:105px;color:var(--white)}
.hero-title{font-family:"Roboto",sans-serif;font-weight:700;font-size:46px;letter-spacing:.5px;line-height:54px}
.hero-text{margin-top:16px;font-size:13.5px;line-height:26px;width:580px}
.btn-outline{display:inline-block;margin-top:24px;border:2px solid var(--white);color:var(--white);font-family:"Roboto",sans-serif;font-size:14px;padding:12px 20px}
.dots{position:absolute;left:100px;top:344px;display:flex;gap:6px}
.dots span{width:16px;height:16px;border-radius:50%;border:2px solid var(--white)}
.dots span.on{background:var(--white)}

/* services */
.services{height:647px;text-align:center;padding-top:68px}
.section-title{font-family:"Roboto",sans-serif;font-weight:700;font-size:25px;color:var(--blue)}
.section-intro{margin:22px auto 0;width:860px;font-size:13.5px;line-height:26px;color:var(--muted)}
.service-row{display:flex;justify-content:center;gap:79px;margin-top:46px}
.service{width:280px}
.drop{width:162px;height:162px;margin:0 auto;border-radius:50% 0 50% 50%;background:var(--grey-icon);display:flex;align-items:center;justify-content:center}
.drop.blue{background:var(--blue)}
.service h3{margin-top:34px;font-family:"Roboto",sans-serif;font-weight:400;font-size:23px;color:#666}
.service h3.blue{color:var(--blue)}
.service p{margin-top:18px;font-size:12.5px;line-height:24px;color:var(--text)}
.btn{display:inline-block;margin-top:22px;background:var(--grey-btn);color:var(--white);font-family:"Roboto",sans-serif;font-size:14px;padding:14px 24px;border-radius:2px}
.btn.blue{background:var(--blue)}

/* how it works */
.how{height:508px;background:linear-gradient(180deg,#3e6bc4 0%,#4b78cc 60%,#4370c6 100%);color:var(--white);text-align:center;padding-top:52px}
.how .section-title{color:var(--white)}
.how .section-intro{color:#e4ebf8;width:900px}
.steps{display:flex;justify-content:center;align-items:flex-start;margin-top:44px}
.step{width:230px;position:relative}
.ring{width:126px;height:126px;border-radius:50%;border:3px solid var(--white);margin:0 auto;display:flex;align-items:center;justify-content:center}
.ring.filled{background:var(--green)}
.num{position:absolute;left:36px;top:-6px;width:36px;height:36px;border-radius:50%;background:var(--green);border:2px solid var(--white);font-family:"Roboto",sans-serif;font-size:17px;line-height:32px}
.step h4{margin-top:24px;font-family:"Roboto",sans-serif;font-weight:500;font-size:17px}
.step p{margin-top:12px;font-size:12.5px;line-height:20px;color:#eef2fb}
.arrow{width:50px;height:126px;display:flex;align-items:center;justify-content:center}

/* uses */
.uses{height:430px;position:relative}
.uses-text{position:absolute;left:100px;top:60px;width:520px}
.uses-title{font-family:"Roboto",sans-serif;font-weight:700;font-size:25px;color:var(--blue)}
.uses-rule{width:170px;height:2px;background:var(--blue);margin-top:14px}
.uses-lead{margin-top:22px;font-family:"Roboto",sans-serif;font-weight:500;font-size:16px;line-height:28px;color:#222}
.uses-list{list-style:none;margin-top:20px}
.uses-list li{display:flex;align-items:center;gap:18px;font-size:12.5px;line-height:26px;color:var(--text)}
.uses-list li::before{content:"";width:8px;height:8px;border:2px solid var(--blue);border-radius:50%}
.streams{position:absolute;left:620px;top:30px;width:500px;height:300px}
.stream-label{position:absolute;font-size:19px;color:#222;text-align:center;line-height:26px}

/* eligibility */
.eligible{height:470px;background:var(--light-bg);text-align:center;padding-top:52px}
.eligible .section-intro{color:#222;width:820px}
.client-row{display:flex;justify-content:flex-start;gap:39px;margin-top:40px;padding-left:100px;text-align:left}
.client{display:flex;gap:18px;width:480px}
.client-photo{width:250px;height:200px;border:4px solid var(--white);flex:none}
.client-photo.roof{background:linear-gradient(180deg,#9cc2d8 0%,#b9a98a 40%,#a8503f 70%,#7a3a30 100%)}
.client-photo.install{background:linear-gradient(180deg,#6a9ed1 0%,#3e6db0 45%,#2f4f86 75%,#c8d3e3 100%)}
.client h3{margin-top:4px;font-family:"Roboto",sans-serif;font-weight:500;font-size:18px;color:#222}
.client p{margin-top:14px;font-size:12px;line-height:24px;color:var(--muted)}
.btn-dark{display:inline-block;margin-top:10px;background:#2e2e2e;color:var(--white);font-family:"Roboto",sans-serif;font-size:11px;padding:8px 24px;border-radius:16px}

/* footer */
.site-footer{height:315px;background:var(--footer);color:var(--white);position:relative}
.footer-brand{position:absolute;left:0;right:0;top:72px;display:flex;justify-content:center;align-items:center;gap:12px}
.footer-brand .brand-square{background:var(--white)}
.footer-brand .brand-name{color:var(--white)}
.footer-nav{position:absolute;left:0;right:0;top:172px;display:flex;justify-content:center;gap:28px;font-family:"Roboto",sans-serif;font-size:16px}
.footer-nav .sep{color:#ddd}
.footer-rule{position:absolute;left:100px;right:100px;top:232px;height:1px;background:#777}
.copyright{position:absolute;left:100px;top:262px;font-size:13px}
.social{position:absolute;right:92px;top:254px;display:flex;gap:8px}
.social span{width:32px;height:32px;border:2px solid var(--white);border-radius:50%}
</style>
</head>
<body>
<div class="page">

<header class="site-header">
  <div class="brand"><span class="brand-square"></span><span class="brand-name">BRIGHTLEAF HOMES</span></div>
  <div class="contact">
    <div class="item mail"><span class="dot"><svg width="16" height="12" viewBox="0 0 16 12"><rect x="1" y="1" width="14" height="10" fill="none" stroke="#fff" stroke-width="1.6"/><path d="M1 1l7 6 7-6" fill="none" stroke="#fff" stroke-width="1.6"/></svg></span>info@brightleafhomes.org</div>
    <div class="item phone"><span class="dot"><svg width="14" height="14" viewBox="0 0 14 14"><path d="M3 1l2.5 3-1.5 1.5c1 2 2.5 3.5 4.5 4.5L10 8.5l3 2.5-1.5 2C6 13 1 8 1 2.5z" fill="#222"/></svg></span>180 555 014</div>
  </div>
  <nav class="main-nav"><span class="active">HOME</span><span>ABOUT US</span><span>SERVICES</span><span>BLOG</span><span>NEWS</span><span>CONTACT US</span></nav>
</header>

<section class="hero">
  <div class="photo" role="img" aria-label="Rows of solar panels on a green grass field with a wind turbine under a pale sky"></div>
  <div class="hero-content">
    <h1 class="hero-title">BRIGHTLEAF HOMES</h1>
    <p class="hero-text">Brightleaf Homes, based on the City of Marrowvale's successful program, ensures that pension card households receive a solar system.</p>
    <span class="btn-outline">READ MORE</span>
  </div>
  <div class="dots"><span class="on"></span><span></span><span></span><span></span></div>
</section>

<section class="services">
  <h2 class="section-title">BRIGHTLEAF HOMES SERVICES</h2>
  <p class="section-intro">We are started in support with Victorian councils and four greenhouse alliances to support low income households to install solar systems with no upfront costs.</p>
  <div class="service-row">
    <div class="service">
      <div class="drop"><svg width="80" height="80" viewBox="0 0 80 80" fill="none" stroke="#fff" stroke-width="3"><circle cx="40" cy="40" r="16"/><path d="M40 8v10M40 62v10M8 40h10M62 40h10M17 17l7 7M56 56l7 7M63 17l-7 7M24 56l-7 7"/><path d="M43 30l-7 11h8l-6 10" stroke-linejoin="round"/></svg></div>
      <h3>Safe Solar</h3>
      <p>Brightleaf Homes is a pioneering approach by councils to support pensioner households to save money and take control.</p>
      <span class="btn">READ MORE</span>
    </div>
    <div class="service">
      <div class="drop blue"><svg width="80" height="80" viewBox="0 0 80 80" fill="#fff"><rect x="14" y="14" width="15" height="11"/><rect x="32" y="14" width="15" height="11"/><rect x="50" y="14" width="15" height="11"/><rect x="14" y="28" width="15" height="11"/><rect x="32" y="28" width="15" height="11"/><rect x="50" y="28" width="15" height="11"/><rect x="14" y="42" width="15" height="11"/><rect x="32" y="42" width="15" height="11"/><rect x="50" y="42" width="15" height="11"/><rect x="37" y="55" width="6" height="10"/><rect x="26" y="65" width="28" height="4"/></svg></div>
      <h3 class="blue">Reliable Solar</h3>
      <p>Brightleaf Homes is a pioneering approach by councils to support pensioner households to save money and take control.</p>
      <span class="btn blue">READ MORE</span>
    </div>
    <div class="service">
      <div class="drop"><svg width="80" height="80" viewBox="0 0 80 80" fill="none" stroke="#fff" stroke-width="3"><circle cx="40" cy="38" r="17"/><path d="M40 6v8M12 38h8M60 38h8M19 17l6 6M61 17l-6 6"/><path d="M34 56h12v8H34z"/><path d="M35 32v6M45 32v6M33 38h14v4a7 7 0 0 1-14 0z"/></svg></div>
      <h3>Trustworthy</h3>
      <p>Brightleaf Homes is a pioneering approach by councils to support pensioner households to save money and take control.</p>
      <span class="btn">READ MORE</span>
    </div>
  </div>
</section>

<section class="how">
  <h2 class="section-title">HOW DOES IT WORK</h2>
  <p class="section-intro">Help pensioner households to save money and take control of their energy bills by installing an affordable, quality solar system and be part of an Australian first.</p>
  <div class="steps">
    <div class="step">
      <span class="num">1</span>
      <div class="ring"><svg width="60" height="60" viewBox="0 0 60 60" fill="none" stroke="#fff" stroke-width="2.5"><circle cx="30" cy="30" r="12"/><path d="M30 6v8M30 46v8M6 30h8M46 30h8M13 13l6 6M41 41l6 6M47 13l-6 6M19 41l-6 6"/><path d="M26 25v5M34 25v5M24 30h12v3a6 6 0 0 1-12 0z"/></svg></div>
      <h4>Checking</h4>
      <p>Brightleaf Homes checks that every person gets a solar system that pays for itself in energy savings.</p>
    </div>
    <div class="arrow"><svg width="40" height="26" viewBox="0 0 40 26"><path d="M0 9h24V0l16 13-16 13v-9H0z" fill="#fff"/></svg></div>
    <div class="step">
      <span class="num">2</span>
      <div class="ring filled"><svg width="60" height="60" viewBox="0 0 60 60" fill="none" stroke="#fff" stroke-width="2.5"><circle cx="30" cy="30" r="20" stroke-dasharray="4 3"/><circle cx="30" cy="30" r="12"/><path d="M22 26h16M22 34h16M30 18v24"/></svg></div>
      <h4>Organising</h4>
      <p>Brightleaf Homes organises for the solar system to be installed.</p>
    </div>
    <div class="arrow"><svg width="40" height="26" viewBox="0 0 40 26"><path d="M0 9h24V0l16 13-16 13v-9H0z" fill="#fff"/></svg></div>
    <div class="step">
      <span class="num">3</span>
      <div class="ring"><svg width="60" height="60" viewBox="0 0 60 60" fill="none" stroke="#fff" stroke-width="2.5"><circle cx="30" cy="22" r="11"/><path d="M10 54c0-12 9-18 20-18s20 6 20 18z"/></svg></div>
      <h4>Support</h4>
      <p>Brightleaf Homes supports pensioners to understand and get the most out of solar.</p>
    </div>
    <div class="arrow"><svg width="40" height="26" viewBox="0 0 40 26"><path d="M0 9h24V0l16 13-16 13v-9H0z" fill="#fff"/></svg></div>
    <div class="step">
      <span class="num">3</span>
      <div class="ring"><svg width="60" height="60" viewBox="0 0 60 60" fill="none" stroke="#fff" stroke-width="2.5"><rect x="22" y="8" width="26" height="30" rx="2"/><path d="M35 14v20M39 18h-6a3 3 0 0 0 0 6h4a3 3 0 0 1 0 6h-6"/><path d="M8 44h10l8 4h12a3 3 0 0 1 0 6H22M8 54h30l12-8"/></svg></div>
      <h4>Payment</h4>
      <p>Pensioners gradually pay for cost through their usual rates payments at 0% interest.</p>
    </div>
  </div>
</section>

<section class="uses">
  <div class="uses-text">
    <h2 class="uses-title">USES OF BRIGHTLEAF HOME</h2>
    <div class="uses-rule"></div>
    <p class="uses-lead">Brightleaf Homes will support councils to install solar for pension card households by:</p>
    <ul class="uses-list">
      <li>coordinating household promotion and recruitment</li>
      <li>responding to householder enquiries</li>
      <li>managing the procurement process to contract a solar installer</li>
      <li>administering the installations</li>
      <li>securing lower interest finance options for households</li>
      <li>evaluating the project</li>
    </ul>
  </div>
  <svg class="streams" viewBox="0 0 500 300" role="img" aria-label="Illustration of two payment streams: a lender and supplier funding a home, and a council and supplier funding a home">
    <g fill="var(--stream-fill)" fill-opacity=".6" stroke="var(--blue)" stroke-width="3"><circle cx="140" cy="140" r="128"/><circle cx="350" cy="140" r="128"/></g>
  </svg>
  <div class="stream-label" style="left:640px;top:338px;width:240px">Private Low Interest<br>Finance Stream</div>
  <div class="stream-label" style="left:858px;top:338px;width:240px">Council Rates Stream</div>
</section>

<section class="eligible">
  <h2 class="section-title">IS MY CLIENT ELIGIBLE?</h2>
  <p class="section-intro">Over 20 Victorian councils have come together with support from the State Clean Power Fund to run the Brightleaf Home program.</p>
  <div class="client-row">
    <div class="client">
      <div class="client-photo roof" role="img" aria-label="Red tiled house roof fitted with solar panels"></div>
      <div>
        <h3>HOMEOWNERS</h3>
        <p>Brightleaf Homes will be progressively rolled out across participating Victorian municipalities through to June 2019. There are 20 participating councils and a limited.</p>
        <span class="btn-dark">CLICK HERE</span>
      </div>
    </div>
    <div class="client">
      <div class="client-photo install" role="img" aria-label="Installer fitting solar panels on a rooftop under blue sky"></div>
      <div>
        <h3>PENSION CARD HOLDERS</h3>
        <p>Brightleaf Homes will be progressively rolled out across participating Victorian municipalities through to June 2019. There are 20 participating councils and a limited.</p>
        <span class="btn-dark">CLICK HERE</span>
      </div>
    </div>
  </div>
</section>

<footer class="site-footer">
  <div class="footer-brand"><span class="brand-square"></span><span class="brand-name">BRIGHTLEAF HOMES</span></div>
  <nav class="footer-nav"><span>HOME</span><span class="sep">|</span><span>SERVICES</span><span class="sep">|</span><span>BLOG</span><span class="sep">|</span><span>ABOUT US</span><span class="sep">|</span><span>NEWS</span><span class="sep">|</span><span>CONTACT US</span></nav>
  <div class="footer-rule"></div>
  <p class="copyright">© 2017 Brightleaf Homes. All Rights Reserved</p>
  <div class="social"><span></span><span></span><span></span><span></span><span></span></div>
</footer>

</div>
</body>
</html>
```